Business Card Design Needed

Business car design required, logo will be supplied.

Brambleford Power Surveyors are looking to become the leading provider of energy performance certificates to estate agents, landlords and home owners in the Yorkshire region of the UK.

The business card must be double sided and professional looking. Estate agents receive hundreds of cards from contractors and our card must stand out.

I require a two sided business card that is clean, modern and created by a designer that can think outside of the box.

Brand colours can be supplied .

Please ask if you have any questions.

Target Market(s)

Estate agents, landlords and property owners

Industry/Entity Type

Property - estate agency - energy consultants

Contact Information for Business Card

Tomas Rendell - Energy Assessor - 07311642705 - www.BramblefordPSV.co.uk - info@bramblefordpsv.co.uk

Font styles to use
Serif
Sans Serif

Colors
00AB8E
00BBA5
67D7C9
C6EFE9
E9F9F6

Requirements
Must have
• Use the provided logo, clean, professional and stand out from the crowd
Nice to have
• Clever use of text, spacing and brand colours
Should not have
• Clip art

```html
<!DOCTYPE html>
<html lang="en">
<head>
<meta charset="utf-8">
<title>Brambleford Power Surveyors – Business Card</title>
<link rel="stylesheet" href="https://fonts.googleapis.com/css2?family=Arimo:wght@400;700&display=swap">
<style>
  :root {
    --page-bg: #e6e7e8;
    --card-white: #ffffff;
    --card-dark: #2a2a2a;
    --card-dark-edge: #383838;
    --brand-blue: #1f6e9e;
    --brand-lime: #a8c51c;
    --text-grey: #6a6a6a;
    --text-light: #f2f2f2;
    --shadow: rgba(0, 0, 0, 0.18);
  }
  * { box-sizing: border-box; margin: 0; padding: 0; }
  html, body {
    width: 1200px;
    height: 900px;
    overflow: hidden;
    background: var(--page-bg);
    font-family: "Arimo", Arial, sans-serif;
  }
  .card-spread {
    position: relative;
    width: 1200px;
    height: 900px;
  }
  .card {
    position: absolute;
    top: 70px;
    width: 440px;
    height: 760px;
    border-radius: 4px;
    box-shadow: 0 14px 34px var(--shadow);
    overflow: hidden;
  }

  /* Front */
  .card--front {
    left: 130px;
    background: var(--card-white);
  }
  .front-brand {
    position: absolute;
    top: 210px;
    left: 48px;
    display: flex;
    align-items: center;
    gap: 18px;
  }
  .brand-dot {
    width: 62px;
    height: 62px;
    border-radius: 50%;
    background: var(--brand-blue);
    flex: none;
  }
  .brand-divider {
    width: 1px;
    height: 70px;
    background: var(--brand-blue);
  }
  .brand-name {
    font-size: 30px;
    line-height: 1.1;
    font-weight: 400;
    color: var(--brand-blue);
    letter-spacing: 0.5px;
  }
  .front-accent-bar {
    position: absolute;
    left: 0;
    top: 500px;
    width: 26px;
    height: 200px;
    background: var(--brand-lime);
    border-radius: 0 12px 12px 0;
  }
  .contact-block {
    position: absolute;
    left: 72px;
    top: 508px;
  }
  .person-name {
    font-size: 34px;
    font-weight: 700;
    color: var(--brand-lime);
    letter-spacing: 0.5px;
  }
  .person-role {
    margin-top: 6px;
    font-size: 24px;
    color: var(--text-grey);
  }
  .role-rule {
    width: 48px;
    height: 2px;
    background: var(--brand-lime);
    margin: 16px 0 18px;
  }
  .contact-list { list-style: none; }
  .contact-list li {
    display: flex;
    align-items: center;
    gap: 14px;
    font-size: 21px;
    color: var(--text-grey);
    margin-bottom: 10px;
  }
  .contact-icon {
    width: 20px;
    height: 20px;
    flex: none;
  }

  /* Back */
  .card--back {
    left: 630px;
    background: var(--card-dark);
  }
  .back-pattern {
    position: absolute;
    inset: 0;
    background: radial-gradient(circle at 70% 80%, #4a4a4a 0%, var(--card-dark-edge) 35%, var(--card-dark) 75%);
  }
  .back-brand {
    position: absolute;
    left: 120px;
    bottom: 96px;
    display: flex;
    align-items: center;
    gap: 14px;
  }
  .back-brand .brand-dot {
    width: 46px;
    height: 46px;
    background: var(--brand-lime);
  }
  .back-brand .brand-divider {
    height: 52px;
    background: var(--text-light);
  }
  .back-brand .brand-name {
    font-size: 22px;
    color: var(--text-light);
  }
</style>
</head>
<body>
<main class="card-spread">

  <section class="card card--front" aria-label="Card front">
    <div class="front-brand">
      <span class="brand-dot"></span>
      <span class="brand-divider"></span>
      <p class="brand-name">Brambleford<br>Power Surveyors</p>
    </div>

    <div class="front-accent-bar"></div>

    <div class="contact-block">
      <h1 class="person-name">TOMAS RENDELL</h1>
      <p class="person-role">Energy Assessor</p>
      <div class="role-rule"></div>
      <ul class="contact-list">
        <li>
          <svg class="contact-icon" viewBox="0 0 24 24" aria-hidden="true">
            <path fill="#a8c51c" d="M6.6 10.8a15 15 0 0 0 6.6 6.6l2.2-2.2c.3-.3.7-.4 1-.2 1.1.4 2.3.6 3.6.6.6 0 1 .4 1 1V20c0 .6-.4 1-1 1A17 17 0 0 1 3 4c0-.6.4-1 1-1h3.5c.6 0 1 .4 1 1 0 1.3.2 2.5.6 3.6.1.3 0 .7-.2 1z"/>
          </svg>
          07311642705
        </li>
        <li>
          <svg class="contact-icon" viewBox="0 0 24 24" aria-hidden="true">
            <circle cx="12" cy="12" r="9" fill="none" stroke="#a8c51c" stroke-width="2"/>
            <path d="M3 12h18M12 3c3 3 3 15 0 18M12 3c-3 3-3 15 0 18" fill="none" stroke="#a8c51c" stroke-width="1.6"/>
          </svg>
          www.BramblefordPSV.co.uk
        </li>
        <li>
          <svg class="contact-icon" viewBox="0 0 24 24" aria-hidden="true">
            <rect x="2" y="5" width="20" height="14" rx="1.5" fill="#a8c51c"/>
            <path d="M2.5 6l9.5 7 9.5-7" fill="none" stroke="#ffffff" stroke-width="1.6"/>
          </svg>
          info@bramblefordpsv.co.uk
        </li>
      </ul>
    </div>
  </section>

  <section class="card card--back" aria-label="Card back">
    <div class="back-pattern" role="img" aria-label="Embossed repeating brand pattern in dark grey gloss"></div>
    <div class="back-brand">
      <span class="brand-dot"></span>
      <span class="brand-divider"></span>
      <p class="brand-name">Brambleford<br>Power Surveyors</p>
    </div>
  </section>

</main>
</body>
</html>
```